Stationary Design to Complement our Website

We would like template designed for word documents that we can use for headed paper. The template should complement the style of our website & incorporate our existing logo. https://www.palvenroutes.com/

The header and footer design should be sperate PNG or JPEG files that we can copy and paste into word header and footers. They should work on A4 & letter sized papers.

Note the main web colours are as follows:

Black
HEX code #2b2c2b
C=71 M=64 Y=64 K=65
RGB 43,44,43

Green
HEX code #116c49
C=88 M=33 Y=82 K=24
RGB 17,108,73

Current fonts are ALEO & Gilroy.

Fonts and colours in new design don't have to match website exactly but should be complementary.
Updates

Made some updates to the brief

Font styles to use
Serif

Requirements
Must have
• a simple design that complements our website.
Some kind of graphic on the top & some sort of graphic on the bottom. Not just plain logo on top.
designs that incorporate the clouds might look good
Can also incorporate 5* rate marsh rating
Should not have
• no photographs included on the design

```html
<!DOCTYPE html>
<html lang="en">
<head>
<meta charset="utf-8">
<title>Palven Routes Letterhead</title>
<link rel="stylesheet" href="https://fonts.googleapis.com/css2?family=Cinzel:wght@500&family=Montserrat:wght@400&family=PT+Sans:wght@400&display=swap">
<style>
  :root {
    --backdrop: #838383;
    --paper: #f6f3f3;
    --ink: #1d1d1d;
    --body-ink: #4a4a4a;
    --brand-green: #116c49;
  }
  html, body {
    margin: 0;
    width: 1072px;
    height: 1200px;
    overflow: hidden;
    background: var(--backdrop);
  }
  .letterhead {
    position: absolute;
    left: 208px;
    top: 124px;
    width: 682px;
    height: 961px;
    background: var(--paper);
    box-shadow: 1px 1px 2px rgba(0,0,0,0.35);
    overflow: hidden;
  }
  .brand {
    position: absolute;
    left: 65px;
    top: 68px;
    display: flex;
    align-items: flex-start;
    gap: 8px;
  }
  .brand-dot {
    width: 14px;
    height: 14px;
    margin-top: 2px;
    border-radius: 50%;
    background: var(--brand-green);
  }
  .brand-name {
    font-family: 'Cinzel', serif;
    font-weight: 500;
    font-size: 27px;
    line-height: 35px;
    letter-spacing: 5px;
    color: var(--ink);
    margin-top: 10px;
  }
  .contact {
    position: absolute;
    top: 106px;
    font-family: 'Montserrat', sans-serif;
    font-size: 9.6px;
    line-height: 12.4px;
    color: var(--ink);
  }
  .contact-address { left: 327px; }
  .contact-lines { left: 512px; }
  .letter {
    position: absolute;
    left: 67px;
    top: 268px;
    width: 550px;
    font-family: 'PT Sans', sans-serif;
    color: var(--body-ink);
  }
  .greeting {
    font-size: 18px;
    margin: 0 0 26px;
    font-weight: 400;
  }
  .letter p {
    font-size: 10.4px;
    line-height: 16.4px;
    margin: 0 0 16.4px;
    text-align: justify;
  }
  .closing {
    margin-top: 33px !important;
  }
  .signature {
    position: absolute;
    left: 67px;
    top: 707px;
    width: 88px;
    height: 36px;
    background: linear-gradient(90deg, rgba(43,44,43,0.12), rgba(43,44,43,0.04));
  }
  .footer-dot {
    position: absolute;
    left: 583px;
    top: 916px;
    width: 34px;
    height: 34px;
    border-radius: 50%;
    background: var(--brand-green);
  }
  .footer-band {
    position: absolute;
    left: 0;
    bottom: 0;
    width: 100%;
    height: 11px;
    background: var(--brand-green);
  }
</style>
</head>
<body>
<div class="letterhead">
  <header>
    <div class="brand">
      <span class="brand-dot"></span>
      <div class="brand-name">Palven<br>Routes</div>
    </div>
    <div class="contact contact-address">4120 Heather Row<br>Brookfield, Oregon 97210<br>www.palvenroutes.com</div>
    <div class="contact contact-lines">T: 555-210-4736<br>F: 555-210-4790<br>hello@palvenroutes.com</div>
  </header>

  <main class="letter">
    <h1 class="greeting">Dear Mr. Hadley,</h1>
    <p>Lorem ipsum dolor sit amet, consectetur adipiscing elit. Donec orci purus, luctus vitae dignissim eu, iaculis sed purus. Vivamus faucibus, ipsum nec aliquet viverra, leo mauris condimentum ligula, sit amet sagittis enim ligula quis arcu. Nam egestas tortor id nisi porttitor mattis. In tortor ante, ultricies in suscipit a, tempus non massa. Vivamus et auctor mi. Fusce vel massa nulla. Phasellus nec eros mauris, et scelerisque orci.</p>
    <p>Donec malesuada orci vitae nulla accumsan porta a id massa. Quisque accumsan iaculis magna sit amet fringilla. Maecenas consequat, magna eget tincidunt semper, odio nibh rutrum mi, id feugiat ante nisi eu risus. Vestibulum nunc orci, rhoncus a placerat in, ultricies in mi. Cras mattis varius eros, vel fringilla nisi suscipit eget. Quisque scelerisque sagittis nulla at porttitor.</p>
    <p>Sed id augue vitae urna euismod commodo aliquet a quam. Pellentesque arcu velit, cursus et malesuada ut, consequat et diam. Nullam erat sem, rhoncus id ullamcorper vitae, rhoncus et arcu. In ultricies ultricies nulla, ut rutrum nisi iaculis at. Donec eu magna a metus ornare faucibus. Fusce aliquet faucibus ultricies. Morbi semper, est id tincidunt gravida, sem arcu adipiscing lacus, ac bibendum nulla leo eu purus. Quisque nec diam sed risus consectetur a ccumsan quis quis nibh. Vestibulum id purus lorem.</p>
    <p>It is a long established fact that a reader will be distracted by the readable content of a page when looking at its layout. The point of using Lorem Ipsum is that it has a more-or-less normal distribution of letters, as opposed to using 'Content here, content here', making it look like readable English. Many desktop publishing packages</p>
    <p class="closing">Sincerely,</p>
  </main>

  <div class="signature" role="img" aria-label="Handwritten signature of the sender"></div>

  <footer>
    <span class="footer-dot"></span>
    <div class="footer-band"></div>
  </footer>
</div>
</body>
</html>
```